Web Design for Small Healthcare Startup

Hello,

We are seeking a Website Design for a healthcare company focusing on mobile vaccinations, employee health and wellness services onsite at businesses, and consulting services relating to Healthcare Entities in WA state. Our company’s mission is to “To aid in a healthier workplace”. Brightpath Rovers will provide on-site wellness services to employers that simplify and streamline employee preventative health as well as onsite consulting services to help with compliance of Healthcare Entities.

We are seeking a Website Design for Brightpath Rovers, PLLC. Our company’s mission is to provide mobile health and wellness services to employers onsite at their businesses. These services include mobile vaccinations clinics for employees as well as wellness and health screenings. The company will also offer healtcare compliance consulting services for Healthcare Entities. The company was founded to bring these important healthcare services to businesses and keep employees healthy. Healthy employees are the cornerstone to a great business and we want to help orginazations achieve their goals of having a healthy productive workforce.

We are looking for a moderin website design that will need to be coded. We have attached our current logo design for reference as well as a brief questionare regarding our business for your information (not necessary to include all information). We would like something SEO friendly and easy to navigate.

Thank you!

Brightpath Rovers, PLLC

Target Market(s)

Small Businesses

Industry/Entity Type

Healthcare

Coding

Coded - Design and coding required

Number of Pages Required

1 page

Requirements
Nice to have
• SEO Friendly, Incorporate Logo

```html
<!DOCTYPE html>
<html lang="en">
<head>
<meta charset="utf-8">
<title>Brightpath Rovers, PLLC – Mobile Workplace Wellness</title>
<link href="https://fonts.googleapis.com/css2?family=Poppins:wght@400;500;600;700&family=Zilla+Slab:wght@700&display=swap" rel="stylesheet">
<style>
:root{
  --blue:#1356a8;
  --purple:#a3479b;
  --ink:#2a2a2a;
  --text:#3a3a3a;
  --white:#ffffff;
  --rule:#f1f3f8;
  --hero-dark:#2c3646;
  --hero-mid:#5a6b82;
}
*{margin:0;padding:0;box-sizing:border-box}
html,body{width:821px;height:1200px;overflow:hidden;background:var(--white)}
body{position:relative;font-family:"Poppins",sans-serif;color:var(--ink)}
.abs{position:absolute}

.site-header{position:absolute;left:0;top:0;width:821px;height:74px;background:var(--white)}
.brand{position:absolute;left:112px;top:26px;display:flex;align-items:center;gap:6px;font-weight:700;font-size:14px;color:var(--blue);white-space:nowrap}
.brand-dot{width:12px;height:12px;border-radius:50%;background:var(--purple)}
.main-nav a{position:absolute;top:28px;font-size:10.5px;color:var(--ink);text-decoration:none}
.btn{position:absolute;display:flex;align-items:center;justify-content:center;border-radius:14px;font-size:10.5px;text-decoration:none}
.btn-purple{background:var(--purple);color:var(--white)}
.btn-white{background:var(--white);color:var(--blue);font-weight:700}

.hero{position:absolute;left:0;top:74px;width:821px;height:359px;
  background:linear-gradient(100deg,var(--hero-dark) 0%,var(--hero-mid) 45%,#7a8aa3 70%,#3b4f8a 100%)}
.hero-title{position:absolute;left:0;width:821px;text-align:center;font-family:"Zilla Slab",serif;font-weight:700;color:var(--white);line-height:1}

.section-title{position:absolute;left:0;width:821px;text-align:center;font-weight:700;font-size:24px;color:var(--blue);line-height:1}

.svc-label{position:absolute;font-size:10.5px;font-weight:500;color:var(--ink);line-height:12px}
.svc-label.right{text-align:right}
.svc-bubble{position:absolute;width:43px;height:43px;border-radius:50%;background:var(--blue)}
.illustration{position:absolute;border-radius:6px;background:linear-gradient(90deg,#e9d5e7,#d5e2f3)}

.section-rule{position:absolute;left:0;top:709px;width:821px;height:3px;background:var(--rule)}
.lead{position:absolute;left:0;width:821px;text-align:center;font-size:9px;color:var(--text);line-height:15.7px}

.site-footer{position:absolute;left:0;top:967px;width:821px;height:202px;background:var(--blue);color:var(--white)}
.footer-brand{position:absolute;left:112px;top:1045px;font-size:13px;font-weight:700;white-space:nowrap;display:flex;align-items:center;gap:5px}
.footer-brand .sq{width:10px;height:10px;background:var(--white)}
.footer-about{position:absolute;left:111px;top:1072px;font-size:9.2px;line-height:14px;width:130px}
.footer-head{position:absolute;top:1014px;font-size:10px;font-weight:600;letter-spacing:.2px}
.footer-head::after{content:"";position:absolute;left:0;top:20px;width:26px;height:1px;background:rgba(255,255,255,.6)}
.footer-link{position:absolute;font-size:9.5px;color:var(--white);text-decoration:none}
.contact-ico{position:absolute;width:25px;height:25px;border:1px solid var(--white);border-radius:50%;display:flex;align-items:center;justify-content:center}
.contact-text{position:absolute;left:474px;font-size:9.5px;line-height:13px}
.social{position:absolute;left:644px;font-size:9.5px;display:flex;align-items:center;gap:7px}
.social i{display:block;width:9px;height:9px;border-radius:50%;background:var(--white)}

.copyright{position:absolute;left:0;top:1169px;width:821px;height:31px;background:var(--purple);color:var(--white);font-size:9.5px;display:flex;align-items:center;justify-content:center}
.copyright b{font-weight:700;margin:0 3px}
</style>
</head>
<body>

<header class="site-header">
  <div class="brand"><span class="brand-dot"></span>Brightpath Rovers</div>
  <nav class="main-nav">
    <a style="left:368px" href="#">Home</a>
    <a style="left:426px" href="#">About Us</a>
    <a style="left:499px" href="#">Services</a>
    <a style="left:568px" href="#">Pricing</a>
  </nav>
  <a class="btn btn-purple" style="left:629px;top:24px;width:82px;height:23px" href="#">Contact Us</a>
</header>

<section class="hero" role="img" aria-label="Healthcare worker in blue gloves giving a vaccine injection into a patient's upper arm">
</section>
<h1>
  <span class="hero-title" style="top:200px;font-size:26px">Making The Workplace</span>
  <span class="hero-title" style="top:237px;font-size:30px">A Healthier Place.</span>
</h1>
<a class="btn btn-white" style="left:370px;top:277px;width:81px;height:28px" href="#">More Info</a>

<h2 class="section-title" style="top:471px">Services We Offer</h2>

<svg class="abs" style="left:0;top:590px" width="821" height="125" viewBox="0 590 821 125">
  <path d="M305 709 A105 105 0 0 1 515 709" fill="none" stroke="#1356a8" stroke-width="1.2"/>
  <g fill="#fff" stroke="#a3479b" stroke-width="1.2">
    <circle cx="410" cy="604" r="2.5"/>
    <circle cx="343" cy="629" r="2.5"/>
    <circle cx="478" cy="629" r="2.5"/>
    <circle cx="310" cy="680" r="2.5"/>
    <circle cx="511" cy="680" r="2.5"/>
  </g>
</svg>

<div class="svc-label" style="left:356px;top:531px">Pneumonia vaccines</div>
<div class="svc-bubble" style="left:389px;top:552px"></div>

<div class="svc-label right" style="left:220px;top:597px;width:68px">Covid<br>Booster</div>
<div class="svc-bubble" style="left:300px;top:589px"></div>

<div class="svc-label" style="left:532px;top:597px">Wellness<br>Screenings</div>
<div class="svc-bubble" style="left:478px;top:589px"></div>

<div class="svc-label right" style="left:120px;top:668px;width:123px">Mobile Vaccine<br>Clinics Providing Flu</div>
<div class="svc-bubble" style="left:255px;top:659px"></div>

<div class="svc-label" style="left:577px;top:668px">Consulting Services For<br>WA Healthcare Entities</div>
<div class="svc-bubble" style="left:523px;top:659px"></div>

<div class="illustration" style="left:345px;top:652px;width:130px;height:57px" role="img" aria-label="Line illustration of a mobile clinic van with a medical cross and syringes"></div>

<div class="section-rule"></div>

<h2 class="section-title" style="top:777px">Avoid long lines …</h2>
<div class="abs" style="left:105px;top:819px;width:54px;height:11px;background:var(--rule)"></div>
<p class="lead" style="top:816px">
  Each employee can sign up for specific time or dept managers can release employees in phases to clinic.<br>
  Also available: book for entire day so employees can get vaccinated as their workload permits.<br>
  Employees will avoid congested waiting rooms at medical offices and long lines at local pharmacies
</p>
<a class="btn btn-purple" style="left:370px;top:874px;width:81px;height:26px;border-radius:13px" href="#">Contact Us</a>

<footer class="site-footer"></footer>
<div class="footer-brand" style="color:var(--white)"><span class="sq"></span>Brightpath Rovers</div>
<p class="footer-about" style="color:var(--white)">Lorem ipsum dolor sit amet, consectetuer adipiscing elit lorem ipsum.</p>

<div class="footer-head" style="left:277px;color:var(--white)">QUICK LINKS</div>
<a class="footer-link" style="left:278px;top:1043px" href="#">+ Home</a>
<a class="footer-link" style="left:335px;top:1043px" href="#">+ Pricing</a>
<a class="footer-link" style="left:278px;top:1067px" href="#">+ About</a>
<a class="footer-link" style="left:335px;top:1067px" href="#">+ Contact Us</a>
<a class="footer-link" style="left:278px;top:1091px" href="#">+ Services</a>

<div class="footer-head" style="left:440px;color:var(--white)">CONTACT DETAILS</div>
<div class="contact-ico" style="left:442px;top:1046px">
  <svg width="11" height="11" viewBox="0 0 24 24"><path fill="#fff" d="M6.6 10.8a15.1 15.1 0 0 0 6.6 6.6l2.2-2.2c.3-.3.7-.4 1-.2 1.1.4 2.3.6 3.6.6.6 0 1 .4 1 1V20c0 .6-.4 1-1 1C10.6 21 3 13.4 3 4c0-.6.4-1 1-1h3.5c.6 0 1 .4 1 1 0 1.3.2 2.5.6 3.6.1.3 0 .7-.2 1z"/></svg>
</div>
<div class="contact-text" style="top:1043px;color:var(--white)">Call Us<br>123 456 7890</div>
<div class="contact-ico" style="left:442px;top:1081px">
  <svg width="11" height="9" viewBox="0 0 24 18"><rect x="1" y="1" width="22" height="16" rx="2" fill="#fff"/><path d="M2 3l10 7 10-7" fill="none" stroke="#1356a8" stroke-width="2"/></svg>
</div>
<div class="contact-text" style="top:1081px;color:var(--white)">Mail Us<br>info@brightpathrovers.com</div>

<div class="footer-head" style="left:644px;color:var(--white)">FOLLOW US</div>
<div class="social" style="top:1045px;color:var(--white)"><i></i>Circlefeed</div>
<div class="social" style="top:1065px;color:var(--white)"><i></i>Chirpline</div>
<div class="social" style="top:1085px;color:var(--white)"><i></i>Reelhouse</div>
<div class="social" style="top:1105px;color:var(--white)"><i></i>Snapgrid</div>

<div class="copyright">Copyright © 2022 <b>Brightpath Rovers PLLC</b>. All Rights Reserved.</div>

</body>
</html>
```